We are a music company that specializes in Music Mixing and Mastering. We also do vocal recording and create instrumentals for various artists. Our website is 738kv.com

Target Market(s)

Musicians, Record labels, rappers, and singers

Industry/Entity Type

Artists

Contact Information for Business Card

738KV
Industry Standard Mixing & Mastering
(555) 214-3907
sales@738kv.com
738kv.com

Requirements
Must have
• contact info and twitter (@738KV)

```html
<!DOCTYPE html>
<html lang="en">
<head>
<meta charset="utf-8">
<title>738KV Business Card</title>
<link rel="stylesheet" href="https://fonts.googleapis.com/css2?family=Roboto+Condensed:wght@700&display=swap">
<style>
  :root {
    --stage: #d9d9db;
    --card-dark: #1a171b;
    --photo-deep: #141116;
    --photo-mid: #4a3f4c;
    --photo-light: #8f8592;
    --brand-red: #d3141c;
  }
  html, body {
    margin: 0;
    width: 1200px;
    height: 900px;
    overflow: hidden;
    background: var(--stage);
  }
  .canvas {
    position: relative;
    width: 1200px;
    height: 900px;
    display: flex;
    align-items: center;
    justify-content: center;
    gap: 40px;
  }
  .card {
    position: relative;
    width: 540px;
    height: 309px;
    overflow: hidden;
    background: var(--card-dark);
    font-family: "Roboto Condensed", "Arial Narrow", sans-serif;
    font-weight: 700;
  }
  .card__photo {
    position: absolute;
    inset: 0;
  }
  .card__photo--keyboard {
    background:
      linear-gradient(160deg, var(--photo-light) 0%, var(--photo-mid) 35%, var(--photo-deep) 80%);
  }
  .card__photo--console {
    background:
      linear-gradient(200deg, var(--photo-deep) 0%, var(--photo-mid) 45%, var(--photo-light) 70%, var(--photo-deep) 100%);
  }

  /* Contact side */
  .contact {
    position: absolute;
    left: 34px;
    top: 54px;
    right: 24px;
    color: var(--brand-red);
    line-height: 1.25;
  }
  .contact__title {
    margin: 0 0 8px;
    font-size: 21px;
  }
  .contact__line {
    display: flex;
    align-items: center;
    gap: 8px;
    font-size: 26px;
    white-space: nowrap;
  }
  .contact__icon {
    width: 24px;
    height: 24px;
    flex: none;
  }

  /* Brand side */
  .brand {
    position: absolute;
    right: 48px;
    top: 46px;
    color: var(--brand-red);
    text-align: right;
  }
  .brand__name {
    margin: 0;
    font-size: 92px;
    line-height: 1;
    letter-spacing: 1px;
  }
  .brand__tagline {
    margin: 4px 0 0;
    font-size: 22px;
  }
</style>
</head>
<body>
<main class="canvas">

  <section class="card card--contact">
    <div class="card__photo card__photo--keyboard" role="img" aria-label="Photo of a synthesizer keyboard with faders and knobs"></div>
    <div class="contact">
      <p class="contact__title">738KV Industry Standard Mixing &amp; Mastering</p>
      <div class="contact__line">
        <svg class="contact__icon" viewBox="0 0 24 24" aria-hidden="true">
          <rect x="2" y="5" width="20" height="14" fill="none" stroke="currentColor" stroke-width="2"/>
          <path d="M2 5 L12 13 L22 5" fill="none" stroke="currentColor" stroke-width="2"/>
        </svg>
        <span>sales@738kv.com</span>
      </div>
      <div class="contact__line">
        <svg class="contact__icon" viewBox="0 0 24 24" aria-hidden="true">
          <circle cx="12" cy="12" r="10" fill="none" stroke="currentColor" stroke-width="2"/>
          <ellipse cx="12" cy="12" rx="4.5" ry="10" fill="none" stroke="currentColor" stroke-width="1.6"/>
          <path d="M2 12 H22 M4 7 H20 M4 17 H20" stroke="currentColor" stroke-width="1.6"/>
        </svg>
        <span>738kv.com</span>
      </div>
      <div class="contact__line">
        <svg class="contact__icon" viewBox="0 0 24 24" aria-hidden="true">
          <path d="M6.6 2.5 L9.5 6.5 L7.8 8.6 C9 11.3 12.7 15 15.4 16.2 L17.5 14.5 L21.5 17.4 L19.5 21 C12 21 3 12 3 4.5 Z" fill="currentColor"/>
        </svg>
        <span>(555) 214-3907</span>
      </div>
      <div class="contact__line">
        <svg class="contact__icon" viewBox="0 0 24 24" aria-hidden="true">
          <circle cx="12" cy="12" r="9" fill="currentColor"/>
        </svg>
        <span>@738KV</span>
      </div>
    </div>
  </section>

  <section class="card card--brand">
    <div class="card__photo card__photo--console" role="img" aria-label="Photo of a large studio mixing console in perspective"></div>
    <div class="brand">
      <p class="brand__name">738KV</p>
      <p class="brand__tagline">Standard Mixing &amp; Mastering</p>
    </div>
  </section>

</main>
</body>
</html>
```